Corporate Business Card

Very professional, Modern, Not to busy, include phone address email, website
(253) 555-0174, 61807 19th Street N, Kent, WA 98517, marcus@kestrelbayholding.com, brelvanindustries.com

Target Market(s)

Manufacturing

Industry/Entity Type

Aero, machining, manufacturing, Off road racing

Contact Information for Business Card

Phone, address email, website

```html
<!DOCTYPE html>
<html lang="en">
<head>
<meta charset="utf-8">
<title>Brelvan Industries — Business Card</title>
<link href="https://fonts.googleapis.com/css2?family=Lato:wght@400;700;900&family=Montserrat:wght@800&display=swap" rel="stylesheet">
<style>
  :root {
    --navy: #1c3a7a;
    --navy-deep: #1f2c63;
    --navy-light: #1d4b8c;
    --red: #d4232b;
    --ink: #1f1f24;
    --paper: #ffffff;
    --stage: #2a2a2c;
    --rule: #555a66;
  }
  * { box-sizing: border-box; margin: 0; padding: 0; }
  html, body {
    width: 1200px; height: 895px; overflow: hidden;
    background: var(--stage);
    font-family: "Lato", Arial, sans-serif;
  }
  .canvas { position: relative; width: 1200px; height: 895px; }

  .card {
    position: absolute; width: 600px; height: 343px; overflow: hidden;
    box-shadow: 0 14px 30px rgba(0,0,0,.45);
  }

  /* Back side */
  .card-back {
    left: 90px; top: 70px;
    background: linear-gradient(160deg, var(--navy-light) 0%, var(--navy-deep) 100%);
    color: var(--paper);
  }
  .card-back .wordmark {
    position: absolute; left: 0; right: 0; top: 112px;
    display: flex; align-items: center; justify-content: center; gap: 14px;
  }
  .card-back .wordmark-square { width: 18px; height: 18px; background: var(--red); }
  .card-back .wordmark-name {
    font-weight: 900; font-size: 46px; letter-spacing: 1px; line-height: 1; white-space: nowrap;
  }
  .card-back .wordmark-rule {
    position: absolute; left: 150px; top: 190px; width: 300px; height: 2px;
    background: var(--paper);
  }
  .card-back .web {
    position: absolute; left: 0; right: 0; bottom: 40px; text-align: center;
    font-size: 16px; letter-spacing: .5px;
  }
  .card-back .web .domain { color: var(--red); }

  /* Front side */
  .card-front { left: 510px; top: 480px; background: var(--paper); }
  .front-wordmark {
    position: absolute; left: 36px; top: 124px; width: 244px;
    display: flex; align-items: center; gap: 9px;
  }
  .front-wordmark .wordmark-square { width: 12px; height: 12px; background: var(--red); flex: none; }
  .front-wordmark .wordmark-name {
    font-weight: 900; font-size: 24px; color: var(--navy); line-height: 1; letter-spacing: .3px;
    white-space: nowrap;
  }
  .front-rule {
    position: absolute; left: 36px; top: 164px; width: 220px; height: 2px; background: var(--navy);
  }
  .divider {
    position: absolute; left: 300px; top: 62px; width: 1px; height: 130px; background: var(--rule);
  }
  .identity { position: absolute; left: 322px; top: 62px; right: 16px; }
  .person-name {
    font-family: "Montserrat", Arial, sans-serif; font-weight: 800; font-size: 22px;
    color: var(--navy); letter-spacing: .3px; line-height: 1;
  }
  .person-name .surname { color: var(--red); }
  .person-role { font-size: 14px; color: var(--ink); margin-top: 5px; }
  .contact-list { list-style: none; margin-top: 16px; }
  .contact-list li {
    display: flex; align-items: center; gap: 10px;
    font-size: 13.5px; color: var(--ink); line-height: 1; margin-bottom: 7px; white-space: nowrap;
  }
  .contact-list svg { width: 12px; height: 12px; flex: none; }

  .address-band {
    position: absolute; left: 0; right: 0; top: 232px; height: 36px;
    background: var(--navy); color: var(--paper);
    display: flex; align-items: center; justify-content: center;
    font-size: 15px; letter-spacing: .4px;
  }
  .base-band {
    position: absolute; left: 0; right: 0; bottom: 0; height: 32px; background: var(--navy);
  }
</style>
</head>
<body>
<main class="canvas">

  <section class="card card-back" aria-label="Card back">
    <div class="wordmark">
      <span class="wordmark-square"></span>
      <span class="wordmark-name">Brelvan Industries</span>
    </div>
    <div class="wordmark-rule"></div>
    <p class="web">www.<span class="domain">brelvanindustries</span>.com</p>
  </section>

  <section class="card card-front" aria-label="Card front">
    <div class="front-wordmark">
      <span class="wordmark-square"></span>
      <span class="wordmark-name">Brelvan Industries</span>
    </div>
    <div class="front-rule"></div>

    <div class="divider"></div>

    <div class="identity">
      <h1 class="person-name">MARCUS <span class="surname">HALE</span></h1>
      <p class="person-role">Founder &amp; CEO</p>
      <ul class="contact-list">
        <li>
          <svg viewBox="0 0 24 24" aria-hidden="true"><path fill="#d4232b" d="M6.6 10.8a15.1 15.1 0 0 0 6.6 6.6l2.2-2.2c.3-.3.7-.4 1-.2 1.1.4 2.3.6 3.6.6.6 0 1 .4 1 1V20c0 .6-.4 1-1 1C10.6 21 3 13.4 3 4c0-.6.4-1 1-1h3.5c.6 0 1 .4 1 1 0 1.3.2 2.5.6 3.6.1.3 0 .7-.2 1l-2.3 2.2z"/></svg>
          (253) 555-0174
        </li>
        <li>
          <svg viewBox="0 0 24 24" aria-hidden="true"><rect x="2.5" y="5" width="19" height="14" rx="1.5" fill="none" stroke="#d4232b" stroke-width="2.2"/><path d="M3 6l9 7 9-7" fill="none" stroke="#d4232b" stroke-width="2.2"/></svg>
          marcus@kestrelbayholding.com
        </li>
        <li>
          <svg viewBox="0 0 24 24" aria-hidden="true"><g fill="none" stroke="#d4232b" stroke-width="2"><circle cx="12" cy="12" r="9.5"/><ellipse cx="12" cy="12" rx="4" ry="9.5"/><path d="M2.5 12h19M4 7h16M4 17h16"/></g></svg>
          brelvanindustries.com
        </li>
      </ul>
    </div>

    <div class="address-band">61807 19th Street N, Kent, WA 98517</div>
    <div class="base-band"></div>
  </section>

</main>
</body>
</html>
```